Business Card Design: recruitment/consultancy for business Marlowin730go

We need a business card design for a new company based in Adelaide Australia called Marlowin730go. Our Business aims to support people over 50 who may be looking for a career change, have been made redundant or generally looking for employment. We will also be working with businesses to provide them with recruiting solutions, job design, recruitment strategies and customised training. we will also be working with volunteering opportunities for those over 50.
We would like to see the E in marlowin730go strong and dominant. The final design should reflect change for the better, better opportunities, today is the day, make way for the new, all aimed at the 50 plus age group.
Colours we are thinking off include green (money, growth) black and white.... we like the idea of black and white photography with a one dominant colour...think of a of a black and white photo of a woman with dominant red lips...that sort of look

Industry/Entity Type

Business

Contact Information for Business Card

Dale, Wendy & Gwen
phone: 0498613205
Marlowin730go@quillmarsh.net
Facebook/Marlowin730go
www.marlowin730go.net.au

```html
<!DOCTYPE html>
<html lang="en">
<head>
<meta charset="utf-8">
<title>Marlowin730go Business Card</title>
<link rel="stylesheet" href="https://fonts.googleapis.com/css2?family=Roboto:wght@300;400;700&display=swap">
<style>
  :root {
    --page: #e4e1dc;
    --card-light: #3c3c3c;
    --card-dark: #0e0e0e;
    --ink: #f2f2f2;
    --ink-soft: #d8d8d8;
    --accent: #e03a45;
    --photo-light: #d9d9d9;
    --photo-dark: #5a5a5a;
  }
  * { margin: 0; padding: 0; box-sizing: border-box; }
  html, body { width: 1200px; height: 858px; overflow: hidden; }
  body {
    background: var(--page);
    font-family: "Roboto", Arial, sans-serif;
    position: relative;
  }
  .card {
    position: absolute;
    top: 274px;
    width: 540px;
    height: 309px;
    border-radius: 4px;
    overflow: hidden;
    box-shadow: 0 10px 28px rgba(0,0,0,0.28);
  }
  .card--front {
    left: 40px;
    background: linear-gradient(160deg, var(--card-light) 0%, #222 55%, var(--card-dark) 100%);
  }
  .card--back {
    left: 620px;
    background: linear-gradient(160deg, #2a2a2a 0%, #0b0b0b 45%, #000 100%);
  }
  .card__art { position: absolute; inset: 0; }
  .brand {
    position: absolute;
    left: 34px;
    top: 30px;
    font-weight: 300;
    font-size: 26px;
    letter-spacing: 0.2px;
    color: var(--ink);
  }
  .team {
    position: absolute;
    right: 34px;
    top: 26px;
    text-align: right;
    font-weight: 300;
    font-size: 21px;
    line-height: 1.15;
    color: var(--ink);
  }
  .contacts {
    position: absolute;
    right: 22px;
    top: 112px;
    list-style: none;
    text-align: right;
    font-weight: 300;
    font-size: 12.5px;
    line-height: 19px;
    color: var(--ink-soft);
  }
  .contacts li { display: flex; justify-content: flex-end; align-items: center; gap: 8px; }
  .contacts svg { width: 10px; height: 10px; flex: none; }
  .brand--back {
    position: absolute;
    left: 0; right: 0;
    top: 50%;
    transform: translateY(-50%);
    text-align: center;
    font-weight: 700;
    font-size: 24px;
    color: var(--ink);
  }
</style>
</head>
<body>

<section class="card card--front" aria-label="Business card front">
  <svg class="card__art" viewBox="0 0 540 309" width="540" height="309">
    <defs>
      <linearGradient id="portraitTone" x1="0" y1="0" x2="1" y2="1">
        <stop offset="0" stop-color="var(--photo-dark)"/>
        <stop offset="0.45" stop-color="var(--photo-light)"/>
        <stop offset="1" stop-color="var(--photo-dark)"/>
      </linearGradient>
    </defs>
    <path d="M0,186 Q300,112 470,309 L0,309 Z" fill="url(#portraitTone)" role="img" aria-label="Black and white portrait of a woman with red lips"/>
    <path d="M0,186 Q300,112 470,309" fill="none" stroke="#ffffff" stroke-width="4"/>
    <path d="M0,180 Q306,104 482,309" fill="none" stroke="var(--accent)" stroke-width="7"/>
  </svg>

  <div class="brand">Marlowin730go</div>

  <div class="team">Dale,<br>Wendy &amp; Gwen</div>

  <ul class="contacts">
    <li>0498613205
      <svg viewBox="0 0 10 10"><path d="M2 0.5 L4 2.5 L3 3.8 Q4.5 6 6.2 7 L7.5 6 L9.5 8 L8 9.5 Q3 9 0.5 2 Z" fill="var(--accent)"/></svg></li>
    <li>Marlowin730go@quillmarsh.net
      <svg viewBox="0 0 10 10"><rect x="0.5" y="2" width="9" height="6.5" fill="var(--accent)"/><path d="M0.5 2 L5 5.5 L9.5 2" fill="none" stroke="#222" stroke-width="0.8"/></svg></li>
    <li>Marlowin730go
      <svg viewBox="0 0 10 10"><circle cx="5" cy="5" r="4" fill="var(--accent)"/></svg></li>
    <li>www.marlowin730go.net.au
      <svg viewBox="0 0 10 10"><circle cx="5" cy="5" r="4.2" fill="none" stroke="var(--accent)" stroke-width="1"/><ellipse cx="5" cy="5" rx="1.8" ry="4.2" fill="none" stroke="var(--accent)" stroke-width="0.8"/><line x1="0.8" y1="5" x2="9.2" y2="5" stroke="var(--accent)" stroke-width="0.8"/></svg></li>
  </ul>
</section>

<section class="card card--back" aria-label="Business card back">
  <div class="brand--back">Marlowin730go</div>
</section>

</body>
</html>
```